Need a landing page design updated

Need an existing landing page perfected, want it too look similar to one of Quenbrook's landing pages in that it flows and is really aesthetically pleasing. The link to the landing page is below. I need this design updated asap. Please take the content directly from the page.

http://verdanthollowsx.com/residential-services/

Target Market(s)

High end residential landscape customers on the gulf coast of Florida (Clearwater area)

Industry/Entity Type

Landscape Gardening

Font styles to use
Sans Serif
Decorative

Requirements
Must have
• I want to keep the written content the same on on the landing page, but would like to work on making both aesthetically appealing to the consumer. This is for high end residential clients on the gulf coast of florida, so think palm trees and sunny beaches with beautiful houses and gorgeous landscapes....look through www.verdanthollowsx.com home page for an example of the houses we landscape.
Nice to have
• Would like it to flow as you scroll similar to Quenbrook's landing pages.
• Look at how Quenbrook's landing page flows, want similar here.....
• https://www.quenbrook.com/tavlo-q/
Should not have
• this landing page must be beautiful and must make a lot of sense as you scroll, am looking for a work of art....please do not submit generic templates or anything that can be easily done....I need real artistry.

```html
<!DOCTYPE html>
<html lang="en">
<head>
<meta charset="utf-8">
<title>Verdant Hollows – Residential Landscaping</title>
<link rel="stylesheet" href="https://fonts.googleapis.com/css2?family=Questrial&family=Quicksand:wght@500;700&display=swap">
<style>
  :root{
    --green:#8cc117;
    --green-soft:#a6d64a;
    --green-deep:#4e9a16;
    --ink:#2b2b2b;
    --muted:#6a6a6a;
    --white:#ffffff;
    --footer:#1c2028;
    --footer-line:#3a3f48;
    --icon-grey:#8a8f97;
    --body-font:'Questrial', sans-serif;
    --head-font:'Quicksand', sans-serif;
  }
  *{box-sizing:border-box;margin:0;padding:0}
  html,body{width:1006px;height:1200px;overflow:hidden;background:var(--white)}
  body{position:relative;font-family:var(--body-font);color:var(--ink)}

  /* Testimonial */
  .testimonial{position:absolute;left:0;top:0;width:1006px;height:255px;background:var(--white)}
  .testimonial__avatar{position:absolute;left:468px;top:31px;width:70px;height:70px;border-radius:50%;
    background:radial-gradient(circle at 50% 40%,#c9b8a6 0%,#8f8f94 60%,#5f6c78 100%)}
  .testimonial__quote{position:absolute;left:168px;width:670px;top:120px;text-align:center;
    font-style:italic;font-size:14px;line-height:21px;color:var(--muted);letter-spacing:.6px}
  .testimonial__name{position:absolute;left:0;width:1006px;top:172px;text-align:center;font-size:11px;letter-spacing:1px;color:var(--ink)}
  .testimonial__arrow{position:absolute;top:154px}
  .testimonial__arrow--prev{left:140px}
  .testimonial__arrow--next{left:848px}

  /* Flaws band */
  .flaws{position:absolute;left:0;top:255px;width:1006px;height:297px;
    background:linear-gradient(180deg,#2f3a24 0%,#3f5a26 40%,#4d7a22 70%,#3c4f24 100%)}
  .flaws__photo{position:absolute;inset:0;
    background:radial-gradient(ellipse at 80% 75%,rgba(150,40,90,.45),transparent 45%),
               radial-gradient(ellipse at 15% 30%,rgba(60,100,40,.6),transparent 50%),
               rgba(0,0,0,.12)}
  .flaws__title{position:absolute;left:0;width:1006px;top:62px;text-align:center;
    font-family:var(--head-font);font-weight:700;font-size:19.5px;line-height:25px;color:var(--white);letter-spacing:1.2px}
  .flaws__rule{position:absolute;left:487px;top:130px;width:32px;height:2px;background:var(--white)}
  .flaws__item{position:absolute;left:168px;display:flex;align-items:center;color:var(--white);font-size:16.5px;letter-spacing:1.25px}
  .flaws__num{width:26px;height:26px;border:2px solid var(--green);border-radius:50%;display:flex;align-items:center;justify-content:center;
    font-family:var(--head-font);font-weight:700;font-size:15px;margin-right:24px;letter-spacing:0}
  .flaws__item--one{top:166px}
  .flaws__item--two{top:210px}

  /* Call to action */
  .cta{position:absolute;left:0;top:552px;width:1006px;height:351px;background:#fdfdfd;overflow:hidden}
  .cta__grass{position:absolute;left:0;bottom:0;width:1006px;height:170px;
    background:linear-gradient(180deg,rgba(166,214,74,0) 0%,rgba(166,214,74,.55) 35%,var(--green-soft) 65%,var(--green-deep) 100%)}
  .cta__title{position:absolute;left:0;width:1006px;top:60px;text-align:center;font-family:var(--head-font);font-weight:700;
    font-size:19.5px;line-height:26px;letter-spacing:1.3px;color:var(--ink)}
  .cta__rule{position:absolute;left:487px;top:119px;width:32px;height:2px;background:var(--green)}
  .cta__lead{position:absolute;left:0;width:1006px;top:133px;text-align:center;font-size:16.3px;letter-spacing:1.2px;color:#444}
  .cta__form{position:absolute;left:306px;top:168px;width:393px}
  .cta__input{display:block;width:393px;height:33px;border:2px solid var(--green);background:var(--white);
    padding-left:16px;font-family:var(--body-font);font-size:14px;color:#aaa;line-height:29px;letter-spacing:.8px;margin-bottom:10px}
  .cta__button{display:block;margin:0 auto;width:114px;height:34px;background:var(--green);color:var(--white);
    font-family:var(--body-font);font-size:14.5px;letter-spacing:.8px;text-align:center;line-height:34px}

  /* Footer */
  .footer{position:absolute;left:0;top:903px;width:1006px;height:297px;background:var(--footer);color:var(--white)}
  .footer__brand{position:absolute;left:160px;top:36px;font-family:var(--body-font);font-size:19px;letter-spacing:1.5px;color:var(--white)}
  .footer__about{position:absolute;left:155px;top:80px;width:226px;font-size:11px;line-height:14px;letter-spacing:.5px}
  .footer__social{position:absolute;left:154px;top:178px;display:flex;gap:13px}
  .footer__social span{width:14px;height:14px;border:1.5px solid var(--icon-grey);border-radius:3px}
  .footer__social span.is-active{border-color:var(--green);border-radius:50%}
  .footer__heading{position:absolute;top:30px;font-family:var(--head-font);font-weight:700;font-size:11px;letter-spacing:1.2px}
  .footer__heading--links{left:429px}
  .footer__heading--contact{left:677px}
  .footer__links{position:absolute;left:427px;top:59px;list-style:none;font-size:10px;letter-spacing:.5px}
  .footer__links li{height:25.6px;line-height:14px}
  .footer__contact{position:absolute;left:674px;top:57px;list-style:none;font-size:10px;letter-spacing:1.1px}
  .footer__contact li{display:flex;align-items:center;height:46px}
  .footer__contact svg{width:18px;margin-right:11px}
  .footer__divider{position:absolute;left:0;top:247px;width:1006px;height:1px;background:var(--footer-line)}
  .footer__copy{position:absolute;left:154px;top:269px;font-size:10px;letter-spacing:.5px}
  .footer__copy em{font-style:normal;color:var(--green)}
  .footer__legal{position:absolute;left:678px;top:269px;display:flex;gap:25px;font-size:10px;letter-spacing:.5px}
</style>
</head>
<body>

<section class="testimonial">
  <div class="testimonial__avatar" role="img" aria-label="Portrait of a smiling client"></div>
  <svg class="testimonial__arrow testimonial__arrow--prev" width="18" height="30" viewBox="0 0 18 30"><polyline points="16,1 2,15 16,29" fill="none" stroke="#8cc117" stroke-width="1.6"/></svg>
  <p class="testimonial__quote">We are delighted with your landscaping, both with the design and implementation.It’s not very often these days that work exceeds expectations.</p>
  <p class="testimonial__name">John Doe</p>
  <svg class="testimonial__arrow testimonial__arrow--next" width="18" height="30" viewBox="0 0 18 30"><polyline points="2,1 16,15 2,29" fill="none" stroke="#8cc117" stroke-width="1.6"/></svg>
</section>

<section class="flaws" role="img" aria-label="Lush residential garden with lawn and flowering beds">
  <div class="flaws__photo"></div>
  <h2 class="flaws__title">Do our services have flaws?<br>Yes. They have two giant ones.</h2>
  <div class="flaws__rule"></div>
  <p class="flaws__item flaws__item--one"><span class="flaws__num">1</span>Your “new” garden will get all of your neighbors jealous.</p>
  <p class="flaws__item flaws__item--two"><span class="flaws__num">2</span>Your friends will probably start inviting themselves over more frequently.</p>
</section>

<section class="cta">
  <div class="cta__grass" role="img" aria-label="Tall green grass with butterflies"></div>
  <h2 class="cta__title">So, what’s the next step to enriching your living area?<br>And getting you a garden from your dreams.</h2>
  <div class="cta__rule"></div>
  <p class="cta__lead">It’s simple, just book a no-obligations consultation</p>
  <div class="cta__form">
    <div class="cta__input">Name</div>
    <div class="cta__input">Email</div>
    <div class="cta__button">Get Started</div>
  </div>
</section>

<footer class="footer">
  <div class="footer__brand">VERDANT HOLLOWS</div>
  <p class="footer__about">Lorem ipsum dolor sit amet, consectetur adipiscing elit, sed do eiusmod tempor incididunt ut labore et dolore magna aliqua. Ut enim ad minim veniam, quis nostrud exercitation ullamco laboris nisi ut aliquip</p>
  <div class="footer__social" aria-label="Social links"><span></span><span></span><span class="is-active"></span><span></span><span></span></div>

  <h3 class="footer__heading footer__heading--links">QUICKLINKS</h3>
  <ul class="footer__links">
    <li>Policy &amp; Support</li>
    <li>Our Projects</li>
    <li>Career &amp; Benfits</li>
    <li>FAQ</li>
    <li>About Us</li>
    <li>Contact Us</li>
  </ul>

  <h3 class="footer__heading footer__heading--contact">GET IN TOUCH</h3>
  <ul class="footer__contact">
    <li><svg viewBox="0 0 18 20" height="20"><path d="M9 19s-6-6.5-6-11a6 6 0 0 1 12 0c0 4.5-6 11-6 11z" fill="none" stroke="#8cc117" stroke-width="1.3"/><circle cx="9" cy="8" r="2.2" fill="none" stroke="#8cc117" stroke-width="1.3"/></svg>Room 214 3rd Floor, Dunmore</li>
    <li><svg viewBox="0 0 18 18" height="18"><path d="M4 2l3 3-2 2c1 2 3 4 5 5l2-2 3 3-2 3C7 15 3 11 2 5z" fill="none" stroke="#8cc117" stroke-width="1.3"/></svg>727-555-0184</li>
    <li><svg viewBox="0 0 18 13" height="13"><rect x="1" y="1" width="16" height="11" fill="none" stroke="#8cc117" stroke-width="1.2"/><polyline points="1,1 9,8 17,1" fill="none" stroke="#8cc117" stroke-width="1.2"/></svg>info@verdanthollowsx.com</li>
  </ul>

  <div class="footer__divider"></div>
  <p class="footer__copy">Copyright Reserved 2017 by <em>Verdant Hollows</em></p>
  <nav class="footer__legal"><span>Home</span><span>Privacy &amp; Policy</span><span>Contact Us</span></nav>
</footer>

</body>
</html>
```